Corvanta512 Business Card Redesign

I want to create a design for brand new business cards, I need something exceptional for clear plastic business card design. Please do not submit without it being on a clear design. Photos of the various logo versions attached.

```html
<!DOCTYPE html>
<html lang="en">
<head>
<meta charset="utf-8">
<title>Corvanta512 Business Card</title>
<link href="https://fonts.googleapis.com/css2?family=Montserrat:wght@400;500;600;700&display=swap" rel="stylesheet">
<style>
  :root {
    --canvas: #dfe5ee;
    --navy: #15203d;
    --navy-deep: #0f1830;
    --gold: #d2ab52;
    --gold-light: #e6c578;
    --text-soft: #b3bde0;
    --text-muted: #9ba5c7;
    --white: #f3f4f8;
    --photo-dark: #1c1f28;
    --photo-warm: #4a3f36;
  }
  * { margin: 0; padding: 0; box-sizing: border-box; }
  html, body { width: 1200px; height: 900px; overflow: hidden; }
  body {
    background: var(--canvas);
    font-family: "Montserrat", sans-serif;
    position: relative;
  }
  .card {
    position: absolute;
    left: 60px; top: 144px;
    width: 1080px; height: 612px;
    border-radius: 22px;
    overflow: hidden;
    box-shadow: 0 18px 40px rgba(20, 30, 60, 0.28);
  }
  .card-art { position: absolute; inset: 0; }
  .brand-name {
    position: absolute;
    left: 70px; top: 424px;
    font-size: 60px; font-weight: 600;
    color: var(--gold);
    letter-spacing: 1px;
  }
  .brand-tagline {
    position: absolute;
    left: 70px; top: 502px;
    font-size: 23px; font-weight: 500;
    color: var(--text-soft);
    letter-spacing: 1.5px;
  }
  .holder { position: absolute; right: 71px; top: 124px; text-align: right; }
  .holder-name {
    font-size: 44px; font-weight: 700;
    color: var(--gold);
    letter-spacing: 2px;
    line-height: 1;
  }
  .holder-title {
    margin-top: 14px;
    font-size: 24px; font-weight: 500;
    color: var(--white);
    letter-spacing: 1.5px;
  }
  .holder-rule {
    margin: 12px 0 0 auto;
    width: 114px; height: 3px;
    background: var(--gold);
  }
  .coverage {
    position: absolute; right: 71px; top: 290px;
    text-align: right;
    font-size: 24px; font-weight: 500;
    color: var(--text-soft);
    letter-spacing: 1.5px;
    line-height: 42px;
  }
  .contacts {
    position: absolute; right: 71px; top: 404px;
    list-style: none;
    text-align: right;
    font-size: 24px; font-weight: 500;
    color: var(--text-muted);
    letter-spacing: 1.5px;
  }
  .contacts li {
    display: flex; align-items: center; justify-content: flex-end;
    gap: 8px; height: 46px;
  }
  .contacts .phone-number { letter-spacing: 5px; }
  .contacts svg { width: 24px; height: 24px; flex: none; }
</style>
</head>
<body>
  <div class="card">
    <svg class="card-art" width="1080" height="612" viewBox="0 0 1080 612">
      <defs>
        <linearGradient id="office-tones" x1="0" y1="0" x2="1" y2="1">
          <stop offset="0" stop-color="#2a2e38"/>
          <stop offset="0.45" stop-color="#4a3f36"/>
          <stop offset="1" stop-color="#15171e"/>
        </linearGradient>
        <linearGradient id="panel-tones" x1="0" y1="0" x2="1" y2="1">
          <stop offset="0" stop-color="#1a2648"/>
          <stop offset="1" stop-color="#0f1830"/>
        </linearGradient>
      </defs>
      <rect width="1080" height="612" fill="url(#office-tones)" role="img" aria-label="Photo of an office window overlooking a city skyscraper"/>
      <path d="M440 0 C 450 300, 600 510, 790 612 L1080 612 L1080 0 Z" fill="url(#panel-tones)"/>
      <path d="M440 0 C 450 300, 600 510, 790 612" fill="none" stroke="#d2ab52" stroke-width="4"/>
    </svg>

    <div class="brand-name">Corvanta512</div>
    <div class="brand-tagline">Available 24/7 Including holidays</div>

    <div class="holder">
      <div class="holder-name">DALE RENNER</div>
      <div class="holder-title">Founder</div>
      <div class="holder-rule"></div>
    </div>

    <div class="coverage">
      <p>Serving clients nationwide</p>
      <p>All 50 states covered</p>
    </div>

    <ul class="contacts">
      <li><span class="phone-number">833-4410-512</span>
        <svg viewBox="0 0 24 24" aria-hidden="true"><path fill="#d2ab52" d="M6.6 10.8a15 15 0 0 0 6.6 6.6l2.2-2.2c.3-.3.7-.4 1-.2 1.1.4 2.3.6 3.6.6.6 0 1 .4 1 1V20c0 .6-.4 1-1 1A17 17 0 0 1 3 4c0-.6.4-1 1-1h3.5c.6 0 1 .4 1 1 0 1.3.2 2.5.6 3.6.1.3 0 .7-.2 1z"/></svg>
      </li>
      <li><span>info@corvanta-512.com</span>
        <svg viewBox="0 0 24 24" aria-hidden="true"><rect x="2" y="5" width="20" height="14" fill="#d2ab52"/><path d="M2 5l10 8 10-8" fill="none" stroke="#15203d" stroke-width="1.6"/></svg>
      </li>
      <li><span>www.corvanta-512.com</span>
        <svg viewBox="0 0 24 24" aria-hidden="true" fill="none" stroke="#d2ab52" stroke-width="1.6"><circle cx="12" cy="12" r="9.5"/><ellipse cx="12" cy="12" rx="4.2" ry="9.5"/><path d="M2.5 12h19M4 7h16M4 17h16"/></svg>
      </li>
    </ul>
  </div>
</body>
</html>
```